Design for three pages of a 12-page 4-color 8.5 x 11 magazine-type booklet

We will be taking the information from a webpage at quillmerefound.org and putting it into a 12-page 4-color 8.5 x 11 magazine-type booklet that will look like an upscale company report. I need to have a design in Photoshop for the cover and two inside pages that I can use as the template for the pages. I likely will also need help putting it together once I start putting the contents into the pages. I may just decide on the content and have the designer create the booklet as an additional freelance contract. First, I need a design for (1) the front cover, (2) one information page taken from information on http://www.quillmerefound.org/qbf-project-management-staff/, and (3) one of the pages that has a researcher from this page on it: http://www.quillmerefound.org/teaching-people-how-to-have/. That's designs for three pages. The designs have to be very professional looking and businesslike. We will be using the booklet to pitch to foundations and philanthropists. The work on the publication itself would be additional freelance work on an hourly basis.

Font styles to use
Serif

Colors

Designer to choose colors to be used in the design.

Requirements
Must have
• Professional look

```html
<!DOCTYPE html>
<html lang="en">
<head>
<meta charset="utf-8">
<title>QBF Project Management Staff</title>
<link href="https://fonts.googleapis.com/css2?family=Playfair+Display:wght@700&family=Source+Sans+3:wght@400;700&display=swap" rel="stylesheet">
<style>
:root{
  --navy:#2b2e84;
  --accent:#1b8ed8;
  --ink:#1d1d1d;
  --paper:#ffffff;
  --backdrop:#2a2a2a;
}
*{box-sizing:border-box;margin:0;padding:0}
html,body{width:948px;height:1200px;overflow:hidden;background:var(--backdrop)}
.page{position:absolute;left:88px;top:102px;width:770px;height:996px;background:var(--paper);font-family:"Source Sans 3",Arial,sans-serif;color:var(--ink)}
.page-title{position:absolute;left:20px;top:34px;width:730px;height:65px;background:var(--navy);color:#fff;font-family:"Playfair Display",Georgia,serif;font-weight:700;font-size:34px;line-height:65px;padding-left:23px;white-space:nowrap}
.condensed{display:inline-block;transform:scaleX(.82);transform-origin:left center}
.staff-card{position:absolute;width:220px}
.role-bar{height:38px;background:var(--navy);border-top-right-radius:38px 38px;color:#fff;font-family:"Playfair Display",Georgia,serif;font-weight:700;font-size:22px;line-height:38px;padding-left:18px;white-space:nowrap}
.role-bar .condensed{transform:scaleX(.84)}
.bio{margin-top:13px;padding-left:5px;font-size:12.4px;line-height:15.2px}
.portrait{float:left;width:122px;height:122px;margin:0 9px 2px 0}
.name{display:block;font-weight:700;font-size:15.5px;line-height:18.5px;margin-top:4px}
.footer-band{position:absolute;left:20px;top:930px;width:730px;height:32px;background:var(--navy)}
.page-number{position:absolute;left:32px;top:921px;width:38px;height:51px;background:var(--accent);color:#fff;font-weight:700;font-size:14px;line-height:51px;text-align:center}
.site-url{position:absolute;right:57px;top:930px;line-height:32px;color:#fff;font-size:14px}
</style>
</head>
<body>
<main class="page">
  <h1 class="page-title"><span class="condensed">QBF Project Management Staff</span></h1>

  <section class="staff-card" style="left:30px;top:133px">
    <h2 class="role-bar"><span class="condensed">Project Director</span></h2>
    <p class="bio"><span class="portrait" role="img" aria-label="Portrait of R. Calder Holt in front of bookshelves" style="background:linear-gradient(135deg,#5a3a22,#8a6a4a 55%,#2b2220)"></span><span class="name">R. Calder<br>Holt, PhD</span>Dr. Holt is the president of QBF. His doctorate is in adult learning and program design. He has written two practical guides on mentoring and team development. Dr. Holt has led internal communications for a mid-sized utility firm, directed an online graduate studies program, and founded and managed two small consulting businesses.</p>
  </section>

  <section class="staff-card" style="left:278px;top:133px">
    <h2 class="role-bar"><span class="condensed">Finance</span></h2>
    <p class="bio"><span class="portrait" role="img" aria-label="Portrait of Lena Ashford" style="background:linear-gradient(135deg,#d9d6cf,#b9a58a 55%,#3a3532)"></span><span class="name">Lena Ashford</span>Lena Ashford spent two decades in budget and contract work for a federal logistics agency, where she received an agency service award and a regional leadership citation. She later helped grow a network of home-goods stores, managed business operations for a large clinic group's phone and data services, and opened a national sales and distribution office for an overseas manufacturer.</p>
  </section>

  <section class="staff-card" style="left:522px;top:133px">
    <h2 class="role-bar"><span class="condensed">Administration</span></h2>
    <p class="bio"><span class="portrait" role="img" aria-label="Portrait of Karen Wexley outdoors" style="background:linear-gradient(135deg,#3f5a2a,#9a7a4a 50%,#c0543a)"></span><span class="name">Karen<br>Wexley</span>Karen Wexley has served as chief executive of a community wellness clinic, head of operations and staffing for a regional food processing company, marketing and communications director for a private professional society, advisor to a nonprofit patient support fund, and board member of a local business association.</p>
  </section>

  <section class="staff-card" style="left:30px;top:511px">
    <h2 class="role-bar"><span class="condensed">Media</span></h2>
    <p class="bio"><span class="portrait" role="img" aria-label="Portrait of Sabrina Castell" style="background:linear-gradient(135deg,#6b9fd1,#a27a66 55%,#2f5fb0)"></span><span class="name">Sabrina<br>Castell</span>Sabrina Castell is the creator and host of Still Here Radio. She is the author of Still Here – A Doubter's Journey Beyond the Veil, a book that helps readers soften their fear of loss, work through grief, and live each day more fully. She brings her experience in broadcast production and publishing to QBF. She also runs a small events business.</p>
  </section>

  <section class="staff-card" style="left:278px;top:511px">
    <h2 class="role-bar"><span class="condensed">Education</span></h2>
    <p class="bio"><span class="portrait" role="img" aria-label="Portrait of Ben Harwick" style="background:linear-gradient(135deg,#1e1e1e,#b8927a 55%,#e6e6e6)"></span><span class="name">Ben<br>Harwick</span>Ben is a middle grades teacher of social studies and reading. He is a graduate of Prairie State University with a degree in English and teacher education. Ben also sits with the QBF Circle of the Council of Lanterns as a developing medium. Guidance received by the circle and the experiences he has reported suggest his abilities will continue to grow over the coming years.</p>
  </section>

  <section class="staff-card" style="left:522px;top:511px">
    <h2 class="role-bar"><span class="condensed">Publications</span></h2>
    <p class="bio"><span class="portrait" role="img" aria-label="Collage of book covers from Wider Horizon Press" style="background:linear-gradient(135deg,#1c2a5a,#c07a2a 50%,#12306a)"></span><span class="name">Wider<br>Horizon<br>Press</span>Wider Horizon Press is a wholly owned publisher that specializes in publishing books by emerging authors in afterlife studies, research, and education. Books published include Guided Contact Sessions, Renewal &amp; Reconnection Grief Work, A Quiet Comet, Facets of Awareness, New Frontiers in Spirit Contact, Spirit Contact: 14 Tested Methods, 70 True Stories, Your Lasting Self, The Joy of Passing, and The Joy of Keeping Close.</p>
  </section>

  <div class="footer-band"></div>
  <div class="page-number">01</div>
  <div class="site-url">www.quillmerefound.org</div>
</main>
</body>
</html>
```